professional business card

A Clean looking business card for a money transfer company. Our company is call Velorix= Transfer + Send = Transcend (next level)
to show professionalism as well as some effects to show digital tech.

1 side to have position, name and address
2 side to have company name and show that we provide money exchange and cross-border money transfer

Target Market(s)

Remittance companies and high net worth individuals

Industry/Entity Type

Finance

Contact Information for Business Card

Name, address, email, title, services- money exchange and cross-border remittance

Requirements
Nice to have
• Digital age feel

```html
<!DOCTYPE html>
<html lang="en">
<head>
<meta charset="utf-8">
<title>Velorix Business Card</title>
<link rel="stylesheet" href="https://fonts.googleapis.com/css2?family=Montserrat:wght@500;600&family=Open+Sans:wght@400;600&display=swap">
<style>
  :root {
    --backdrop: #8a8987;
    --card-navy: #243241;
    --card-navy-deep: #1c2733;
    --accent-cyan: #5ec3d6;
    --text-light: #e9eef2;
    --pattern-light: #3a4a5b;
  }
  * { box-sizing: border-box; margin: 0; padding: 0; }
  html, body { width: 1200px; height: 801px; overflow: hidden; }
  body {
    background: var(--backdrop);
    position: relative;
    font-family: "Open Sans", sans-serif;
  }
  .card {
    position: absolute;
    top: 246px;
    width: 540px;
    height: 309px;
    background: var(--card-navy);
    border-bottom: 2px solid var(--accent-cyan);
    overflow: hidden;
  }
  .card--front { left: 40px; }
  .card--back { left: 620px; }

  /* Front side */
  .brand {
    position: absolute;
    display: flex;
    align-items: center;
    gap: 12px;
  }
  .brand__dot {
    width: 26px; height: 26px;
    border-radius: 50%;
    background: var(--accent-cyan);
  }
  .brand__name {
    font-family: "Montserrat", sans-serif;
    font-weight: 600;
    color: var(--text-light);
    letter-spacing: 0.04em;
    text-transform: uppercase;
  }
  .card--front .brand { left: 40px; top: 130px; }
  .card--front .brand__name { font-size: 34px; }

  .divider {
    position: absolute;
    left: 300px; top: 30px;
    width: 1px; height: 150px;
    background: var(--accent-cyan);
  }
  .contact {
    position: absolute;
    left: 322px; top: 30px;
    color: var(--text-light);
    font-size: 12.5px;
    line-height: 1.5;
  }
  .contact__name {
    font-family: "Montserrat", sans-serif;
    font-weight: 600;
    color: var(--accent-cyan);
    font-size: 17px;
    letter-spacing: 0.03em;
    text-transform: uppercase;
  }
  .contact__title { margin-bottom: 12px; }
  .contact__address { margin-bottom: 12px; }
  .contact__line { display: flex; align-items: center; gap: 8px; }
  .contact__icon { width: 11px; height: 11px; flex: none; }

  .services {
    position: absolute;
    left: 40px; bottom: 26px;
    color: var(--text-light);
    font-size: 13px;
  }
  .services__label { color: var(--accent-cyan); }

  /* Back side */
  .pattern {
    position: absolute; inset: 0;
    background: linear-gradient(120deg, var(--pattern-light) 0%, var(--card-navy) 45%, var(--card-navy-deep) 100%);
  }
  .card--back .brand {
    left: 50%; top: 50%;
    transform: translate(-50%, -50%);
    gap: 16px;
  }
  .card--back .brand__dot { width: 36px; height: 36px; }
  .card--back .brand__name { font-size: 50px; }
</style>
</head>
<body>
  <section class="card card--front" aria-label="Business card front">
    <div class="brand">
      <span class="brand__dot"></span>
      <span class="brand__name">Velorix</span>
    </div>
    <div class="divider"></div>
    <div class="contact">
      <p class="contact__name">Dorian Kessler</p>
      <p class="contact__title">President</p>
      <p class="contact__address">1870 Harbor Crest Way<br>Seabrook CA 92001</p>
      <p class="contact__line">
        <svg class="contact__icon" viewBox="0 0 12 12"><path fill="#e9eef2" d="M2.5 0.8l2 2-1.1 1.4a7 7 0 0 0 4.4 4.4l1.4-1.1 2 2-1.3 1.7C5 11 1 7 0.8 2.1z"/></svg>
        555-014-2281
      </p>
      <p class="contact__line">
        <svg class="contact__icon" viewBox="0 0 12 12"><rect x="0.5" y="2" width="11" height="8" fill="#e9eef2"/><path d="M0.5 2l5.5 4.5 5.5-4.5" fill="none" stroke="#243241" stroke-width="1.2"/></svg>
        d.kessler@velorix.com
      </p>
      <p class="contact__line">
        <svg class="contact__icon" viewBox="0 0 12 12"><circle cx="6" cy="6" r="5.5" fill="#e9eef2"/><path d="M0.5 6h11M6 0.5c-2.5 3-2.5 8 0 11M6 0.5c2.5 3 2.5 8 0 11" fill="none" stroke="#243241" stroke-width="0.9"/></svg>
        www.velorix.com
      </p>
    </div>
    <p class="services"><span class="services__label">services:</span> money exchange and cross-border remittance</p>
  </section>

  <section class="card card--back" aria-label="Business card back">
    <div class="pattern" role="img" aria-label="Embossed repeating brand-mark pattern in tones of slate and navy"></div>
    <div class="brand">
      <span class="brand__dot"></span>
      <span class="brand__name">Velorix</span>
    </div>
  </section>
</body>
</html>
```